KVR Bastion White Paper

We want our text documents to look professional for advertising purposes. We want the White paper to look similar to our Dornwick Basin Study Document attached.

```html
<!DOCTYPE html>
<html lang="en">
<head>
<meta charset="utf-8">
<title>KVR Bastion White Paper</title>
<link href="https://fonts.googleapis.com/css2?family=Hind:wght@400;500&family=Poppins:wght@500;600&display=swap" rel="stylesheet">
<style>
:root{
  --navy:#233f8f;
  --rule-navy:#1f2a6e;
  --sky:#2aa8e0;
  --heading:#1ea0e4;
  --ink:#1e1e1e;
  --paper:#ffffff;
  --backdrop:#c4c4c4;
}
*{margin:0;padding:0;box-sizing:border-box}
html,body{width:1200px;height:779px;overflow:hidden}
body{background:var(--backdrop);position:relative;font-family:"Hind",Arial,sans-serif;color:var(--ink)}
.page{position:absolute;background:var(--paper)}
.page--left{left:31px;top:33px;width:554px;height:718px}
.page--right{left:616px;top:30px;width:555px;height:719px}
.page__top-band{position:absolute;left:0;top:0;width:100%;height:8px;background:var(--navy)}
.page__foot-band{position:absolute;left:0;bottom:0;width:100%;height:40px;background:var(--navy)}
.page__foot-accent{position:absolute;right:0;bottom:0;width:47px;height:40px;background:var(--sky)}
.block{position:absolute}
.lead-quote{left:28px;top:27px;width:500px;font-size:12.2px;line-height:14.1px;letter-spacing:-0.05px}
.callout{left:28px;top:120px;width:497px;height:63px;background:var(--navy);color:#fff;text-align:center;padding-top:10px;font-size:10.8px;line-height:13px}
.callout__source{display:block;margin-top:4px;font-weight:500}
.heading{font-family:"Poppins",Arial,sans-serif;font-weight:500;color:var(--heading);letter-spacing:-0.15px}
.heading--section{font-size:10.2px}
.heading--sub{font-size:10.2px}
.heading--minor{font-size:8.6px}
.body-copy{font-size:8.6px;line-height:10.85px;letter-spacing:-0.08px}
.body-copy p{text-indent:33px}
.body-copy--loose{line-height:12.65px}
sup{font-size:5px;vertical-align:super;line-height:0}
.rule{left:28px;top:27px;width:499px;height:2px;background:var(--rule-navy)}
.refs-label{left:42px;top:600px;display:flex;align-items:center;width:455px;gap:5px;font-family:"Poppins",Arial,sans-serif;font-weight:500;font-size:7.6px;color:var(--heading)}
.refs-label::after{content:"";flex:1;height:1px;background:var(--heading)}
.refs-list{left:38px;top:614px;width:500px;list-style:none;font-size:8.3px;line-height:13.4px;font-style:italic;color:#2a2a2a}
</style>
</head>
<body>

<section class="page page--left">
  <div class="page__top-band"></div>

  <blockquote class="block lead-quote">“While advances have been made in infection control practices, including improved operating room ventilation, sterilization methods, barriers, surgical techniques, and availability of antimicrobial prophylaxis, SSIs remain a substantial cause of morbidity, prolonged hospitalization, and death. SSI is associated with a mortality rate of 3% and 75% of SSI associated deaths are directly attributable to SSI.” ~ NISB <sup>i</sup></blockquote>

  <div class="block callout">“More than 20,000 deaths per year are due to SSIs, and the chance of<br>death in a surgical patient is doubled if an SSI occurs”
    <span class="callout__source">~ Halvorsen University College of Medicine, Dept. of Surgery <sup>ii</sup></span>
  </div>

  <h2 class="block heading heading--section" style="left:28px;top:206px">I. MAJOR SURGICAL SITE INFECTION PROBLEM IN THE U.S.</h2>
  <div class="block body-copy" style="left:28px;top:232px;width:500px">
    <p>America wastes billions of dollars annually on post-operative surgical site infection expenses, especially related to open abdominal surgeries. Surgical site infection (“SSI”) slows the recovery rate for patients and adds additional health costs to facilities with prolonged hospital treatment, additional home care, physician office and emergency room visits expenses.</p>
    <p>Open surgeries are more susceptible to high infection rates and slow patient recovery periods which also impact physicians, staff, hospitals, insurers, etc. Moreover, SSI costs hospitals billions of dollars every year in the U.S. and insurance companies do not reimburse hospitals for maladies caused by infection, and corresponding complications due to SSI.</p>
    <p>“Surgical site infections (SSI) are among the most common health care-associated infections. Surgical site infections account for 20% to 31% of health care-associated infections in hospitalized patients and have considerable morbidity, a mortality rate of 3%, stays prolonged by 7 to 10 days, and costs $20,000 to $27,000 per admission. Reducing SSIs is a national priority, as reflected in the National Council for Health Services’ National Action Plan to Prevent Healthcare-Associated Infections.” ~ Journal of Clinical Surgical Practice <sup>iii</sup></p>
  </div>

  <h2 class="block heading heading--section" style="left:29px;top:390px">II. CURRENT SOLUTIONS</h2>
  <h3 class="block heading heading--minor" style="left:29px;top:414px">A. Open Wound and Drainage Treatments</h3>
  <div class="block body-copy" style="left:29px;top:437px;width:500px">
    <p>Surgeons often respond to the high risk of SSI with various open wound and drainage techniques; they do not close the incision area following surgery to allow oxygen into the impacted area. The patient is left with a hole in their body that is open to the outside; restricting patients from normal activity and subjecting them to psychological distress of knowing and often visibly seeing their own open wound. Open wounds require daily wound care cleanings and dressing changes, antibiotics and often high cost wound vac treatments for one to two weeks or longer.</p>
    <p>Physicians, in attempts to avoid an open wound, will often install a drainage device either by cutting an additional incision into the patient or by placing a drain laterally inside the wound. This is accomplished by placing a plastic tube into the patient, horizontally along the fascia layer and closing the wound around the tube. The most common drains -- the “J-Drain”, and “Penrose Drain” -- have a tendency to clog up and can even increase the production of additional fluid in patients and consequently the colonization of pathogens, defeating the purpose of the drains. The drains must then be removed by surgeon sometimes a week or more after surgery.</p>
    <p>While antibiotics are useful to patient recoveries and are routinely administered prior to and following surgeries, and in conjunction with other preventative measures, pathogens can adapt to antibiotics which has reduced their effectiveness as a preventive measure.</p>
  </div>

  <h3 class="block heading heading--sub" style="left:29px;top:599px">B. Negative Pressure Therapy Devices</h3>
  <div class="block body-copy" style="left:29px;top:624px;width:500px">
    <p>Recently, “negative pressure therapy” (NPT) devices are often touted as the standard of care for closed incision as well as open wound infection preventative treatments. NPT devices remove excess fluid from surface areas from the outer skin level but can be subject to complications.iv NPT devices are very expensive, physician and nurse-labor intensive, subjected to numerous recalls and often require capital expenditures. In addition, their effectiveness is now being questioned by some clinicians. <sup>v</sup></p>
  </div>

  <div class="page__foot-band"></div>
  <div class="page__foot-accent"></div>
</section>

<section class="page page--right">
  <div class="page__top-band"></div>
  <div class="block rule"></div>

  <h3 class="block heading heading--sub" style="left:28px;top:45px">C. Wound Packing Techniques</h3>
  <div class="block body-copy" style="left:28px;top:73px;width:500px">
    <p>In an attempt to protect their patients, some surgeons use various wound packing techniques to varying degrees of success. These physicians are making their own customized materials, cutting strips and soaking them in various solutions in advance of surgery to protect patients from SSI as best they can. Material retention after surgery is also a concern. While these surgeons are implementing their own materials and methods to help protect their patients, acting on their own they could be placing patients and themselves at additional risk due to non-standardized procedures, material retention, and lack of official oversight.</p>
  </div>

  <h2 class="block heading heading--section" style="left:28px;top:149px">III. A NEW APPROACH IS NEEDED TO LOWER HEALTHCARE COSTS AND REDUCE SSI RATES.</h2>
  <h3 class="block heading heading--sub" style="left:28px;top:177px">A. Wound Packing Study</h3>
  <div class="block body-copy body-copy--loose" style="left:28px;top:204px;width:500px">
    <p>Dornwick Basin Health network (“Dornwick Study”) conducted a clinical trial on the effectiveness of wound packing. The Dornwick Study involved a high-risk patient group in open colon resection surgeries, a high-risk SSI surgery category, involving a detailed wound packing technique developed over years of case studies. The patient group was comprised of individuals with a variety of high SSI risk factors: steroids/immunosuppressants, some contaminated wounds, blood transfusions, more than 50% had stomas, and an average age of 65.6 and average BMI of 29.</p>
    <p>Despite the presence of multiple SSI risk factors and high SSI risk colon sectioning procedures, and the fact that all the patients had their incisions closed with sutures or staples immediately following surgery, the patient group using wound packing resulted in a 2.2% overall infection rate, an 84% reduction in SSI overall, down from 14.2% which was the institution’s control SSI rate. The study had only one case of superficial infection in the study group and zero cases of deep tissue infection. KVR Bastion™ was designed and developed based on the Dornwick Study, and has been patented and cleared by the FDA, and is available for use on clean-contaminated and contaminated wounds and adult patients and pediatrics.</p>
  </div>

  <h3 class="block heading heading--sub" style="left:28px;top:356px">B. Subcutaneous Dressing Technology: KVR Bastion™</h3>
  <div class="block body-copy body-copy--loose" style="left:28px;top:384px;width:432px">
    <p>Subcutaneous dressing technology absorbs fluids from multiple points from the facia layer and above – along the incision site. The subcutaneous dressing transports fluid and debris external to the body and absorbed into the dressing on top of the wound. After the subcutaneous device is removed, the fistulae created by the device forms a channel for the removal of additional fluids and debris.</p>
    <p>KVR Bastion™ device is a single-use disposable that features surgical packing strips that are treated with anti-MRSA PHMB Polyhexamethlene Biguanide. With the device, the surgical strips are physically attached to a silver alginate dressing. KVR Bastion™ is made in the United States.</p>
    <p>KVR Bastion™ is applied on patients only once immediately following surgery. Packing strips are inserted into the wound and is removed two days later. After that only light dressings and standard wound cleaning methods are employed.</p>
    <p>The device can used for clean-contaminated and contaminated incisions. Extra incisions are not needed in the patient, open wound procedures are used only infrequently, and capital rentals and purchases are eliminated.</p>
    <p>KVR Bastion can be used on a partial procedure listing including abdominal, trauma and many cancer surgeries, stomach and digestive tract, gallbladder, small intestine, large intestine, appendix, liver, pancreas, esophagus, colon, bladder, prostate, uterus, ovaries, kidney, caesarian section and pediatric procedures.</p>
  </div>

  <div class="block refs-label">REFERENCES</div>
  <ol class="block refs-list">
    <li><sup>i</sup> https://www.nisb-health.org/manuals/ssi-current-guide.pdf</li>
    <li><sup>ii</sup> https://halvorsen.edu/medicine/departments/surgery/research/surgical-infections/</li>
    <li><sup>iii</sup> https://clinsurgpractice.org/journal/articles/4471902</li>
    <li><sup>iv</sup> http://www.woundcarereview.net/files/npt-uses-and-possible-complications.pdf</li>
    <li><sup>v</sup> https://medresearchmethods.net/articles/10.5512/mrm-2008-08-04</li>
  </ol>

  <div class="page__foot-band"></div>
  <div class="page__foot-accent"></div>
</section>

</body>
</html>
```